Kestrel Ridgeway Flyer Design

we are a new garden maintenance and landscaping business we are honest hard working and reliable phone 0479315268 email tobias.wren@kestrelmail.com.au we maintain and mow lawns landscape gardens we can help with most handyman jobs were professional reliable and hardworking
Updates

is it possible to have everything greyscale except logo leave that as colour please

Reason: I am making the job non refundable

Target Market(s)

we target everyone from the everyday mowing to the landscaping of showpiece gardens

Industry/Entity Type

Landscaping

Other font styles liked:
• copperplate or engravers

Requirements
Must have
• our logo
my email tobias,wren@kestrelmail.com.au
mobile 0479315268

```html
<!DOCTYPE html>
<html lang="en">
<head>
<meta charset="utf-8">
<title>Kestrel Ridgeway Flyer</title>
<link rel="stylesheet" href="https://fonts.googleapis.com/css2?family=Noto+Serif:wght@400&family=Open+Sans:wght@400&display=swap">
<style>
  :root {
    --page: #ffffff;
    --ink: #111111;
    --white: #ffffff;
    --logo-green: #4f9a3a;
    --logo-brown: #5a3a22;
  }
  .flyer--colour {
    --band-dark: #2b6e22;
    --band-light: #4a9a37;
    --lawn-dark: #5d9a2c;
    --lawn-light: #9ccd52;
    --mower: #2a2a2a;
    --accent: #2c6b26;
    --contact: #4a311d;
  }
  .flyer--grey {
    --band-dark: #3a3a3a;
    --band-light: #6a6a6a;
    --lawn-dark: #5f5f5f;
    --lawn-light: #a9a9a9;
    --mower: #2b2b2b;
    --accent: #3c3c3c;
    --contact: #2f2f2f;
  }
  * { margin: 0; padding: 0; box-sizing: border-box; }
  html, body { width: 1200px; height: 805px; overflow: hidden; background: var(--page); }
  .canvas { position: relative; width: 1200px; height: 805px; }
  .flyer { position: absolute; top: 66px; width: 470px; height: 662px; background: var(--white); overflow: hidden; }
  .flyer--colour { left: 69px; }
  .flyer--grey { left: 666px; }

  .header-band { position: absolute; left: 0; top: 0; width: 470px; height: 128px;
    background: linear-gradient(90deg, var(--band-dark), var(--band-light) 55%, var(--band-dark)); }
  .lawn-photo { position: absolute; left: 0; top: 128px; width: 470px; height: 240px;
    background: radial-gradient(ellipse at 40% 20%, var(--lawn-light), var(--lawn-dark) 80%); }
  .mower-photo { position: absolute; left: 228px; top: 176px; width: 222px; height: 172px;
    border-radius: 40% 30% 20% 20%;
    background: radial-gradient(ellipse at 55% 65%, var(--mower), transparent 70%); opacity: .85; }

  .logo-disc { position: absolute; left: 174px; top: 25px; width: 114px; height: 114px;
    border-radius: 50%; background: var(--white); }
  .name-plate { position: absolute; left: 57px; top: 124px; width: 314px; height: 58px;
    border-radius: 18px; background: var(--white); text-align: center; padding-top: 6px; }
  .name-plate__name { font-family: "Noto Serif", serif; font-size: 25px; line-height: 28px;
    color: var(--logo-green); letter-spacing: .5px; }
  .name-plate__line { font-family: "Noto Serif", serif; font-size: 13.5px; line-height: 16px;
    color: var(--logo-brown); letter-spacing: .3px; }

  .slogan { position: absolute; left: 23px; top: 202px; font-family: "Noto Serif", serif;
    font-size: 20px; line-height: 40px; color: var(--white); }
  .slogan span { display: block; }
  .slogan span + span { padding-left: 38px; }

  .services-tab { position: absolute; left: 0; top: 382px; width: 160px; height: 31px;
    border-radius: 0 16px 16px 0; background: var(--accent); color: var(--white);
    font-family: "Open Sans", sans-serif; font-size: 18px; line-height: 31px; padding-left: 44px; }
  .services-list { position: absolute; top: 430px; list-style: none;
    font-family: "Open Sans", sans-serif; font-size: 17px; line-height: 21px; color: var(--ink); }
  .services-list--left { left: 28px; }
  .services-list--right { left: 246px; }
  .services-list li { position: relative; padding-left: 17px; }
  .services-list li::before { content: ""; position: absolute; left: 0; top: 6px;
    width: 10px; height: 10px; background: var(--accent); }

  .contact-band { position: absolute; left: 0; top: 514px; width: 470px; height: 103px;
    background: var(--contact); color: var(--white); text-align: center; font-family: "Noto Serif", serif; }
  .contact-band__phone { font-size: 27px; line-height: 32px; margin-top: 14px; }
  .contact-band__email { font-size: 18px; line-height: 24px; margin-top: 10px; }
  .footer-band { position: absolute; left: 0; top: 617px; width: 470px; height: 45px;
    background: linear-gradient(90deg, var(--band-light), var(--band-dark) 50%, var(--band-light)); }
</style>
</head>
<body>
<div class="canvas">

  <section class="flyer flyer--colour">
    <div class="header-band"></div>
    <div class="lawn-photo" role="img" aria-label="Photo of a freshly mown striped green lawn"></div>
    <div class="mower-photo" role="img" aria-label="Photo of a petrol lawn mower"></div>
    <div class="logo-disc"></div>
    <div class="name-plate">
      <div class="name-plate__name">KESTREL RIDGEWAY</div>
      <div class="name-plate__line">GARDEN MAINTENANCE &amp; LANDSCAPE</div>
    </div>
    <p class="slogan"><span>Any job you don't wanna do</span><span>we will do it for you.</span></p>
    <div class="services-tab">Services:</div>
    <ul class="services-list services-list--left">
      <li>Lawn mowing</li><li>Pool Cleaning</li><li>Gutter Cleaning</li>
    </ul>
    <ul class="services-list services-list--right">
      <li>Cleanups</li><li>Garden Landscaping</li><li>and more....</li>
    </ul>
    <div class="contact-band">
      <p class="contact-band__phone">Call 0479315268</p>
      <p class="contact-band__email">Email : tobias.wren@kestrelmail.com.au</p>
    </div>
    <div class="footer-band"></div>
  </section>

  <section class="flyer flyer--grey">
    <div class="header-band"></div>
    <div class="lawn-photo" role="img" aria-label="Greyscale photo of a freshly mown striped lawn"></div>
    <div class="mower-photo" role="img" aria-label="Greyscale photo of a petrol lawn mower"></div>
    <div class="logo-disc"></div>
    <div class="name-plate">
      <div class="name-plate__name">KESTREL RIDGEWAY</div>
      <div class="name-plate__line">GARDEN MAINTENANCE &amp; LANDSCAPE</div>
    </div>
    <p class="slogan"><span>Any job you don't wanna do</span><span>we will do it for you.</span></p>
    <div class="services-tab">Services:</div>
    <ul class="services-list services-list--left">
      <li>Lawn mowing</li><li>Pool Cleaning</li><li>Gutter Cleaning</li>
    </ul>
    <ul class="services-list services-list--right">
      <li>Cleanups</li><li>Garden Landscaping</li><li>and more....</li>
    </ul>
    <div class="contact-band">
      <p class="contact-band__phone">Call 0479315268</p>
      <p class="contact-band__email">Email : tobias.wren@kestrelmail.com.au</p>
    </div>
    <div class="footer-band"></div>
  </section>

</div>
</body>
</html>
```